Bright Path Attorneys Billboard Design for Personal Injury Law Firm

Need a billboard design that we can use for different versions. 1400px X 400px jpeg or png
I have attached the logo and the attorney for the billboard. Attorney Marla Benning
Here is a link to our current website brightpathlegalgroup.example

HEADLINE: HIT BY A TRUCK?
SUBHEAD: NO FEE. BIG FIGHT.
877-GRANTLY

HEADLINE: ACCIDENT?
SUBHEAD: NO FEE, UNLESS WE WIN!
877-GRANTLY

HEADLINE: BIG TRUCK. BIG CASE.
SUBHEAD: YOU PAY $0 UPFRONT
877-GRANTLY

Target Market(s)

People in Car Accident

Industry/Entity Type

Personal Injury Attorneys

```html
<!DOCTYPE html>
<html lang="en">
<head>
<meta charset="utf-8">
<title>Bright Path Attorneys – Billboard Concepts</title>
<link href="https://fonts.googleapis.com/css2?family=Poppins:wght@600;800&display=swap" rel="stylesheet">
<style>
  :root {
    --page: #ffffff;
    --band: #fdbe23;
    --accent: #f9b200;
    --ink: #0b0b0b;
    --white: #ffffff;
    --steel-light: #8a8a8a;
    --steel-mid: #4a4a4a;
  }
  * { margin: 0; padding: 0; box-sizing: border-box; }
  html, body { width: 832px; height: 1200px; overflow: hidden; background: var(--page); }
  body { position: relative; font-family: "Poppins", Arial, sans-serif; }

  .accent-band { position: absolute; inset: 0; width: 832px; height: 1200px; }

  .concept-number {
    position: absolute; left: 20px;
    font-weight: 800; font-size: 38px; line-height: 1;
    color: var(--accent);
  }

  .billboard {
    position: absolute; left: 9px; width: 812px; height: 231px;
    background: var(--ink); overflow: hidden;
  }
  .billboard--featured { box-shadow: 0 8px 12px rgba(0,0,0,.45); }

  .billboard__photo { position: absolute; top: 0; right: 0; height: 100%; }
  .photo--truck-front {
    width: 100%;
    background:
      radial-gradient(ellipse 140px 130px at 690px 120px, #b9b9b9 0%, #777 45%, transparent 75%),
      linear-gradient(90deg, #050505 0%, #1d1d1d 35%, #5c5c5c 62%, #9a9a9a 80%, #3a3a3a 100%);
  }
  .photo--wrecked-car {
    width: 340px;
    background:
      radial-gradient(ellipse 150px 70px at 210px 140px, #9d9d9d 0%, #5d5d5d 50%, transparent 80%),
      linear-gradient(90deg, var(--ink) 0%, #222 40%, #2a2a2a 100%);
  }
  .photo--truck-side {
    width: 300px;
    background:
      radial-gradient(ellipse 110px 110px at 170px 120px, #4d4d4d 0%, #2c2c2c 55%, transparent 85%),
      linear-gradient(90deg, var(--ink) 0%, #1f1f1f 45%, #2b2b2b 100%);
  }

  .billboard__copy { position: absolute; left: 0; top: 0; width: 100%; height: 100%; }
  .headline, .subhead, .phone {
    position: absolute; white-space: nowrap; font-weight: 800; line-height: 1;
  }
  .headline { color: var(--white); letter-spacing: -0.5px; }
  .subhead { color: var(--accent); font-weight: 800; }
  .phone { color: var(--accent); letter-spacing: -0.5px; }

  .brand {
    position: absolute; display: flex; align-items: center; gap: 8px;
    color: var(--white); font-weight: 600; font-size: 14px; letter-spacing: 0.3px;
    white-space: nowrap;
  }
  .brand__dot { width: 14px; height: 14px; border-radius: 50%; background: var(--white); }
</style>
</head>
<body>

<svg class="accent-band" viewBox="0 0 832 1200" aria-hidden="true">
  <polygon points="832,218 0,1009 0,1200 68,1200 832,459" fill="var(--band)"/>
</svg>

<!-- Concept 1 -->
<div class="concept-number" style="top:18px;">1.</div>
<section class="billboard billboard--featured" style="top:65px;">
  <div class="billboard__photo photo--truck-front" role="img" aria-label="Black and white photo of a semi truck speeding toward the viewer with motion-blur streaks"></div>
  <div class="billboard__copy">
    <h1 class="headline" style="left:35px; top:30px; font-size:56px;">HIT BY A TRUCK?</h1>
    <p class="subhead" style="left:47px; top:92px; font-size:37px;">NO FEE, BIG FIGHT</p>
    <p class="phone" style="left:34px; top:134px; font-size:66px;">877-GRANTLY</p>
    <div class="brand" style="left:607px; top:198px;"><span class="brand__dot"></span>BRIGHT PATH ATTORNEYS</div>
  </div>
</section>

<!-- Concept 2 -->
<div class="concept-number" style="top:432px;">2.</div>
<section class="billboard" style="top:482px;">
  <div class="billboard__photo photo--wrecked-car" role="img" aria-label="Black and white photo of a sedan with a crushed front end after a collision"></div>
  <div class="billboard__copy">
    <h1 class="headline" style="left:45px; top:33px; font-size:62px;">ACCIDENT?</h1>
    <p class="subhead" style="left:55px; top:101px; font-size:26px;">NO FEE, UNLESS WE WIN!</p>
    <p class="phone" style="left:42px; top:132px; font-size:60px;">877-GRANTLY</p>
    <div class="brand" style="left:605px; top:15px;"><span class="brand__dot"></span>BRIGHT PATH ATTORNEYS</div>
  </div>
</section>

<!-- Concept 3 -->
<div class="concept-number" style="top:844px;">3.</div>
<section class="billboard" style="top:900px;">
  <div class="billboard__photo photo--truck-side" role="img" aria-label="Dark photo of a semi truck parked in front of a building"></div>
  <div class="billboard__copy">
    <h1 class="headline" style="left:28px; top:36px; font-size:48px;">BIG TRUCK, BIG CASE.</h1>
    <p class="subhead" style="left:38px; top:102px; font-size:28px;">YOU PAY $0 UPFRONT</p>
    <p class="phone" style="left:27px; top:134px; font-size:56px;">877-GRANTLY</p>
    <div class="brand" style="left:607px; top:198px;"><span class="brand__dot"></span>BRIGHT PATH ATTORNEYS</div>
  </div>
</section>

</body>
</html>
```